Leadership Brenvale Brochure Design*

We host a local leadership development program every two years. We need a brochure to promote the program. We would like it to be 8 1/2 x 11, tri-fold. I have attached a Word document with the necessary info for the brochure. The brochure will be professionally printed. We would like the final design to be in InDesign.

Target Market(s)

Potential participants of our leadership program. They will be local leaders, male and female, from 30-60 years of age.

Requirements
Must have
• Content as detailed in the Word document attached. Our logo.
Nice to have
• A design that is attractive to young professionals.

```html
<!DOCTYPE html>
<html lang="en">
<head>
<meta charset="utf-8">
<title>Leadership Brenvale Tri-fold Brochure</title>
<link href="https://fonts.googleapis.com/css2?family=Nunito+Sans:wght@400;600;700;800&family=Oswald:wght@600&display=swap" rel="stylesheet">
<style>
:root{
  --navy:#1e2b5e;
  --orange:#f0892d;
  --yellow:#f5dc55;
  --blue:#2f9ad8;
  --green:#3daa47;
  --olive:#6b6f4a;
  --gray:#a9abae;
  --paper:#ebebeb;
  --white:#ffffff;
  --ink:#2b2b2b;
  --bg:#e6e4e0;
}
*{box-sizing:border-box;margin:0;padding:0}
html,body{width:1200px;height:900px;overflow:hidden;background:var(--bg)}
body{font-family:"Nunito Sans",Arial,sans-serif;color:var(--ink);position:relative}
.spread{position:absolute;top:225px;width:582px;height:450px;display:flex;box-shadow:0 2px 8px rgba(0,0,0,.18)}
.spread--outside{left:12px}
.spread--inside{left:606px}
.panel{position:relative;width:194px;height:450px;overflow:hidden}
.panel__bg{position:absolute;inset:0;width:100%;height:100%}
.abs{position:absolute}

/* logo */
.logo{display:flex;align-items:center;gap:4px}
.logo__dot{width:20px;height:20px;border-radius:50%;background:var(--green);flex:none}
.logo__name{font-weight:800;color:var(--navy);font-size:10px;line-height:1.02;text-transform:uppercase;letter-spacing:.2px}

/* outside panel 1 */
.info{left:10px;width:178px;display:flex;gap:6px}
.info__icon{width:22px;flex:none}
.info__title{color:var(--orange);font-weight:800;font-size:10px;margin-bottom:2px}
.info__text{color:var(--white);font-size:6.1px;line-height:1.32}
.info__text p+p{margin-top:6px}

/* testimonials */
.alumni__title{right:10px;top:18px;text-align:right;color:var(--orange);font-weight:800;font-size:11px;line-height:1.15}
.portrait{width:64px;height:64px;border-radius:50%;border:3px solid var(--white);background:radial-gradient(circle at 50% 45%,#b9b9b9,#6d6d6d)}
.alumni__name{font-size:6.3px;line-height:1.3;color:var(--white)}
.alumni__name b{font-weight:700}
.alumni__name i{font-style:italic}
.alumni__quote{font-size:5.6px;line-height:1.33;color:var(--white)}

/* cover */
.cover-quote{left:10px;right:10px;top:322px;text-align:center;color:var(--white);font-weight:700;font-size:10.2px;line-height:1.3}
.sponsor{right:10px;top:402px;text-align:right;color:var(--white);font-size:5.6px;font-weight:700;line-height:1.35}
.sponsor__label{color:var(--orange);font-size:7.2px;font-weight:800}

/* inside */
.section-title{font-family:"Oswald",Impact,sans-serif;font-weight:600;font-size:15px;letter-spacing:.1px}
.section-title--green{color:var(--green)}
.section-title--orange{color:var(--orange)}
.body-text{font-size:6.2px;line-height:1.32;color:var(--ink)}
.list{padding-left:9px;font-size:6.2px;line-height:1.3}
.list li{margin:0}

.event{margin-bottom:9px}
.event__bar{display:flex;height:9px;font-size:6px;color:var(--white);margin-bottom:3px}
.event__date{background:var(--green);padding:0 4px;width:56px;line-height:9px}
.event__time{flex:1;background:var(--gray);text-align:right;padding:0 5px;line-height:9px}
.event__title{font-weight:700;font-size:7.3px;line-height:1.15;color:#1b1b1b}
.event .list{font-size:6px;line-height:1.25}
</style>
</head>
<body>

<!-- OUTSIDE SPREAD -->
<section class="spread spread--outside">

  <div class="panel panel--info" style="background:var(--navy)">
    <svg class="panel__bg" viewBox="0 0 194 450">
      <polygon points="14,10 194,0 194,16 20,26 14,20" fill="var(--orange)"/>
    </svg>

    <div class="abs info" style="top:44px">
      <svg class="info__icon" viewBox="0 0 22 26">
        <circle cx="10" cy="6" r="4" fill="var(--blue)"/>
        <path d="M3 20c0-5 3-8 7-8s7 3 7 8z" fill="var(--blue)"/>
        <path d="M13 14l3 3 5-6" stroke="var(--white)" stroke-width="1.4" fill="none"/>
        <rect x="1" y="23" width="16" height="1.6" fill="var(--green)"/>
      </svg>
      <div>
        <h3 class="info__title">Attendance Policy</h3>
        <div class="info__text"><p>Attendance at all sessions including the opening retreat is compulsory. Participants may miss no more than one session to graduate; however, the Organizational Retreat is mandatory.</p></div>
      </div>
    </div>

    <div class="abs info" style="top:124px">
      <svg class="info__icon" viewBox="0 0 22 26">
        <rect x="2" y="2" width="17" height="13" fill="none" stroke="var(--blue)" stroke-width="1.3"/>
        <path d="M5 11l4-4 3 3 4-5" stroke="var(--blue)" stroke-width="1.2" fill="none"/>
        <circle cx="8" cy="18" r="2.5" fill="var(--blue)"/>
        <rect x="1" y="23" width="16" height="1.6" fill="var(--green)"/>
      </svg>
      <div>
        <h3 class="info__title">Tuition</h3>
        <div class="info__text"><p>If accepted in the Leadership Brenvale program, you or your employer/sponsor will be invoiced $400 for Chamber members and $500 for non-members. This fee covers costs for the retreat, classroom sessions, lunches, and graduation. No refunds will be provided for participants who drop out of the program or do not fulfill the required curriculum.</p></div>
      </div>
    </div>

    <div class="abs info" style="top:262px">
      <svg class="info__icon" viewBox="0 0 22 26">
        <rect x="4" y="1" width="13" height="12" fill="none" stroke="var(--blue)" stroke-width="1.2"/>
        <path d="M7 5h7M7 8h7" stroke="var(--blue)" stroke-width="1"/>
        <rect x="1" y="14" width="20" height="7" fill="none" stroke="var(--blue)" stroke-width="1.1"/>
        <rect x="1" y="23" width="16" height="1.6" fill="var(--green)"/>
      </svg>
      <div>
        <h3 class="info__title">To Apply</h3>
        <div class="info__text">
          <p>Applications are available on the Chamber’s website, www.BrenvaleChamber.com. Applications are due by November 2, 2020.<br>Class size is limited. All applications received by the deadline will be reviewed and final participants for the Leadership Brenvale class will be contacted on December 4, 2020. However, all applicants will be notified of the status of their application in writing.</p>
          <p style="margin-top:10px">For questions, please call the Chamber, 555-014-2290.</p>
        </div>
      </div>
    </div>
  </div>

  <div class="panel panel--alumni" style="background:var(--navy)">
    <svg class="panel__bg" viewBox="0 0 194 450">
      <polygon points="0,30 194,0 194,335 0,225" fill="var(--orange)"/>
      <polygon points="50,110 194,60 194,160" fill="var(--navy)"/>
    </svg>
    <h2 class="abs alumni__title">What Community<br>Alumni Are<br>Saying</h2>
    <div class="abs portrait" role="img" aria-label="Portrait photo of alumna Dana Whitlock" style="left:12px;top:40px"></div>
    <p class="abs alumni__name" style="left:12px;top:112px"><b>Dana Whitlock</b><br><i>Co-Owner, Hollis Smokehouse</i></p>
    <p class="abs alumni__quote" style="left:12px;width:172px;top:134px">“Leadership Brenvale was an awesome experience! I learned many interesting things about the county that I have lived in all my life. We had very informative panel discussions and the tours of local attractions, including the Alder Ridge Correctional Facility were eye opening! I enjoyed learning and working beside a great group of folks who are taking leadership roles in our communities to make our county a better place to live, work and play.”</p>
    <div class="abs portrait" role="img" aria-label="Portrait photo of alumnus Grant R. Ellison" style="left:12px;top:224px"></div>
    <p class="abs alumni__name" style="left:100px;top:232px;width:90px"><b>Grant R. Ellison</b>, CPA,<br><i>Partner/Manager of the Marlow Office<br>Avery Lund &amp; Associates, LLP</i></p>
    <p class="abs alumni__quote" style="left:12px;width:174px;top:312px">“For the first year and a half I was working at Avery Lund, I commuted from Harbor Point, so I was not involved in the community at all. Once we moved here, I knew I wanted and felt I had to become more involved. I learned about the program through a colleague. I couldn’t have asked for a better experience and it really exposed me to the many ways that I could get involved and contribute to the chamber and our community. I didn’t know a soul in that 2014 class when it started and now many of them are my very best friends. If you have an opportunity to go through Leadership Brenvale you would be crazy to pass it up. It is the best program the Chamber has and, quite frankly, one of the best opportunities to better yourself in this community.”</p>
  </div>

  <div class="panel panel--cover" style="background:var(--white)">
    <svg class="panel__bg" viewBox="0 0 194 450">
      <defs>
        <linearGradient id="boatsTone" x1="0" y1="0" x2="1" y2="1">
          <stop offset="0" stop-color="#f7e46c"/><stop offset="1" stop-color="#f1d443"/>
        </linearGradient>
      </defs>
      <polygon points="0,118 194,20 194,305 0,420" fill="url(#boatsTone)" role="img" aria-label="Photo of paper boats on a yellow surface, one blue boat leading"/>
      <polygon points="115,40 194,0 194,14 112,52" fill="var(--blue)"/>
      <polygon points="30,118 194,35 194,52 34,132" fill="var(--orange)"/>
      <polygon points="0,450 0,345 194,245 194,450" fill="var(--navy)"/>
      <polygon points="20,360 194,270 194,286 24,374" fill="var(--orange)"/>
      <polygon points="90,292 194,238 194,252 94,304" fill="var(--blue)"/>
    </svg>
    <div class="abs logo" style="left:12px;top:22px"><span class="logo__dot"></span><span class="logo__name">Leadership<br>Brenvale</span></div>
    <p class="abs cover-quote">“The greatest wealth of a community lies not in the amount of its treasure, but in the quality of its leadership.”</p>
    <p class="abs sponsor"><span class="sponsor__label">Sponsored by:</span><br>Eastridge Community College<br>Brenvale Chamber of Commerce and Tourism</p>
  </div>
</section>

<!-- INSIDE SPREAD -->
<section class="spread spread--inside">
  <svg class="abs" style="left:0;top:0;width:420px;height:210px;z-index:2" viewBox="0 0 420 210">
    <defs>
      <linearGradient id="groupTone" x1="0" y1="0" x2="0" y2="1">
        <stop offset="0" stop-color="#c9b9a0"/><stop offset=".55" stop-color="#8f7a63"/><stop offset="1" stop-color="#5b4e45"/>
      </linearGradient>
    </defs>
    <polygon points="0,0 420,0 300,200 0,200" fill="url(#groupTone)" role="img" aria-label="Group photo of the program class standing together in a meeting room"/>
    <polygon points="380,0 420,0 330,150 316,150" fill="var(--green)" opacity=".9"/>
  </svg>

  <div class="panel panel--overview" style="background:var(--paper)">
    <div class="abs" style="left:0;bottom:0;width:194px;height:16px;background:var(--orange)"></div>
    <h2 class="abs section-title section-title--green" style="left:12px;top:212px">Program Overview</h2>
    <p class="abs body-text" style="left:12px;top:238px;width:172px">Leadership Brenvale is a leadership certification program designed to prepare the leaders of tomorrow. During the five-month program, participants get an in-depth view of community issues, develop leadership skills necessary to assume leadership roles, and are exposed to community involvement opportunities. Leadership Brenvale will provide participants with the opportunities to:</p>
    <ul class="abs list" style="left:12px;top:336px;width:172px">
      <li>Build and demonstrate leadership and communication skills</li>
      <li>Think critically about key business, policy, and civic issues facing Brenvale County</li>
      <li>Build meaningful, long-lasting connections</li>
      <li>Establish ongoing dialogues with experienced community leaders</li>
    </ul>
  </div>

  <div class="panel panel--schedule" style="background:var(--paper)">
    <div class="abs" style="left:0;bottom:0;width:194px;height:16px;background:var(--blue)"></div>
    <h2 class="abs section-title section-title--orange" style="left:12px;top:212px">Schedule:</h2>
    <div class="abs" style="left:12px;top:240px;width:172px">
      <div class="event">
        <div class="event__bar"><span class="event__date">January 17</span><span class="event__time">10:00 a.m. - 7:00 p.m.</span></div>
        <h4 class="event__title">Organizational Retreat &amp; Dinner<br>(Attendance Mandatory)</h4>
        <ul class="list"><li>Introductions</li><li>Team Building</li><li>Motivation</li><li>Leadership Styles</li><li>Social Hour/Dinner</li></ul>
      </div>
      <div class="event">
        <div class="event__bar"><span class="event__date">January 31</span><span class="event__time">8:30 a.m. - 4:00 p.m.</span></div>
        <h4 class="event__title">Business &amp; Industry</h4>
        <ul class="list"><li>Business &amp; Industry Panel</li><li>Tour of Keltron Manufacturing facility</li><li>Tour of Ridgeway Tool Company</li><li>“Taking your vision into B&amp;I”</li></ul>
      </div>
    </div>
  </div>

  <div class="panel panel--dates" style="background:var(--white)">
    <svg class="panel__bg" viewBox="0 0 194 450">
      <polygon points="0,0 22,0 0,60" fill="var(--olive)"/>
      <polygon points="22,0 42,0 0,110 0,60" fill="var(--orange)"/>
      <polygon points="194,385 194,405 155,440 148,432" fill="var(--green)"/>
      <polygon points="194,415 194,432 170,450 158,450" fill="var(--orange)"/>
    </svg>
    <div class="abs logo" style="right:12px;top:18px"><span class="logo__dot"></span><span class="logo__name">Leadership<br>Brenvale</span></div>
    <div class="abs" style="left:12px;top:72px;width:172px">
      <div class="event">
        <div class="event__bar"><span class="event__date">February 21</span><span class="event__time">8:30 a.m. - 4:00 p.m.</span></div>
        <h4 class="event__title">Education</h4>
        <ul class="list"><li>Tour of selected programs at ECC</li><li>College Career Program overview</li><li>Lunch at Brenvale Career and College Academy</li><li>Tour of BCCA</li><li>Overview of CTE program paths</li></ul>
      </div>
      <div class="event">
        <div class="event__bar"><span class="event__date">March 14</span><span class="event__time">8:30 a.m. - 4:00 p.m.</span></div>
        <h4 class="event__title">Future Technologies &amp; Communications</h4>
        <ul class="list"><li>ECC Presents interview</li><li>Trends and forecasts</li><li>Marketing &amp; communications panel</li></ul>
      </div>
      <div class="event">
        <div class="event__bar"><span class="event__date">April 4</span><span class="event__time">8:30 a.m. - 4:00 p.m.</span></div>
        <h4 class="event__title">Government</h4>
        <ul class="list"><li>Overview of state/federal government</li><li>Overview of city/county government</li><li>Tour of Alder Ridge Correctional Institute</li><li>Tour of courthouse</li><li>Judicial presentations</li></ul>
      </div>
      <div class="event">
        <div class="event__bar"><span class="event__date">May 2</span><span class="event__time">8:30 a.m. - 4:00 p.m.</span></div>
        <h4 class="event__title">Health &amp; Wellness</h4>
        <ul class="list"><li>Tour of Lower Bay Hospice</li><li>Community Wellness Roundtable</li><li>Tour of Marren Cancer Care Center</li><li>Virtual Medicine Tutorial</li><li>Tour of BRHS</li></ul>
      </div>
      <div class="event">
        <div class="event__bar"><span class="event__date">May 18</span><span class="event__time">12:00 p.m.</span></div>
        <h4 class="event__title">Graduation Ceremony and Luncheon</h4>
        <ul class="list" style="width:150px"><li>Participants are encouraged to invite their employer/supervisor/mentor/special guest (x2)</li></ul>
      </div>
    </div>
  </div>
</section>

</body>
</html>
```